Business card design needed

A business card and logo for my energy healing practice Tarrawin's Healing Spring. It should match my website www.tarrawinshealingspring-example.com in colours and atmosphere. It should look at bit rustic in combination with nature linking in with the natural healing techniques I offer in a heritage country town in NSW Australia. My business also includes a directory of other health and healing practitioners 'The Spring'. It would be nice if a graphic impression of the attached picture of the water feature in my front yard can be used.

Industry/Entity Type

Health

Contact Information for Business Card

Tarrawin's Healing Spring, Delphine Ashcroft, 14 Larchfield St, Kelbrook NSW 2590, M. 0491 363 718, info@tarrawinshealingspring-example.com, www.tarrawinshealingspring-example.com,
Energy Healing - Your Natural Heritage
Facebook/Twitter see Capital Renewal

```html
<!DOCTYPE html>
<html lang="en">
<head>
<meta charset="utf-8">
<title>Tarrawin's Healing Spring — Business Card</title>
<link rel="stylesheet" href="https://fonts.googleapis.com/css2?family=PT+Sans:ital,wght@0,400;0,700;1,400&display=swap">
<style>
  :root {
    --page: #ffffff;
    --slate-deep: #2e4246;
    --slate-mid: #7f9598;
    --mist: #c8cac9;
    --ink-light: #ffffff;
    --rule: rgba(255,255,255,0.85);
    --stroke-tone: #8d9799;
  }
  html, body { margin: 0; padding: 0; }
  body {
    width: 1200px; height: 900px; overflow: hidden;
    background: var(--page); position: relative;
    font-family: "PT Sans", sans-serif; color: var(--ink-light);
  }
  .card {
    position: absolute; overflow: hidden;
    box-shadow: 0 1px 4px rgba(0,0,0,0.35);
  }
  .card--front {
    left: 38px; top: 113px; width: 414px; height: 687px;
    background: linear-gradient(180deg, var(--slate-deep) 0%, #5f7679 14%, var(--slate-mid) 32%, #a7b2b3 62%, var(--mist) 100%);
  }
  .card--back {
    left: 474px; top: 248px; width: 684px; height: 414px;
    background: linear-gradient(180deg, #33474b 0%, #6f8488 28%, #9eabad 58%, var(--mist) 100%);
  }
  .texture { position: absolute; }
  .brand {
    position: absolute; margin: 0; font-weight: 400; color: var(--ink-light);
    text-shadow: 0 1px 2px rgba(0,0,0,0.35); line-height: 1; white-space: nowrap;
  }
  .card--front .brand__line1 { left: 18px; top: 30px; font-size: 42px; }
  .card--front .brand__line2 { left: 72px; top: 84px; font-size: 42px; }
  .card--back .brand__line1 { left: 76px; top: 126px; font-size: 64px; }
  .card--back .brand__line2 { left: 160px; top: 206px; font-size: 64px; }
  .rule { position: absolute; left: 52px; width: 310px; height: 2px; background: var(--rule); }
  .frame-side { position: absolute; top: 168px; width: 2px; height: 490px; background: var(--rule); }
  .frame-side--left { left: 31px; }
  .frame-side--right { left: 387px; }
  .line {
    position: absolute; left: 0; width: 414px; text-align: center; margin: 0;
    text-shadow: 0 1px 2px rgba(0,0,0,0.3); white-space: nowrap;
  }
  .services { top: 160px; font-size: 28px; line-height: 38px; }
  .practitioner { top: 267px; font-size: 24px; font-style: italic; }
  .address { top: 334px; font-size: 24px; line-height: 34px; }
  .phone { top: 444px; font-size: 37px; font-weight: 700; letter-spacing: 0.5px; }
  .web { top: 520px; font-size: 16px; font-weight: 700; line-height: 31px; letter-spacing: -0.2px; }
  .social {
    position: absolute; left: 0; top: 610px; width: 414px;
    display: flex; justify-content: center; align-items: center; gap: 8px;
    font-size: 23px; text-shadow: 0 1px 2px rgba(0,0,0,0.3);
  }
  .social__mark { width: 28px; height: 28px; background: #3d6f9a; display: inline-block; }
</style>
</head>
<body>

<section class="card card--front" aria-label="Business card front">
  <svg class="texture" style="left:0;top:70px" width="140" height="90" role="img" aria-label="Brush-stroke impression of the water feature stones">
    <polygon points="0,40 130,5 135,35 5,80" fill="var(--stroke-tone)" opacity="0.35"/>
  </svg>
  <svg class="texture" style="left:230px;top:540px" width="184" height="147" role="img" aria-label="Brush-stroke impression of the water feature stones">
    <polygon points="20,147 40,80 184,0 184,147" fill="var(--stroke-tone)" opacity="0.45"/>
  </svg>

  <h1 class="brand brand__line1">Tarrawin's</h1>
  <p class="brand brand__line2">Healing Spring</p>

  <div class="rule" style="top:152px"></div>
  <div class="frame-side frame-side--left"></div>
  <div class="frame-side frame-side--right"></div>

  <p class="line services">• Energy Healing<br>• Your Natural Heritage</p>
  <div class="rule" style="top:252px"></div>
  <p class="line practitioner">Delphine Ashcroft</p>
  <div class="rule" style="top:315px"></div>
  <p class="line address">14 Larchfield St,<br>Kelbrook NSW 2590</p>
  <div class="rule" style="top:424px"></div>
  <p class="line phone">M. 0491 363 718</p>
  <div class="rule" style="top:502px"></div>
  <p class="line web">info@tarrawinshealingspring-example.com<br>www.tarrawinshealingspring-example.com</p>
  <div class="social">
    <span class="social__mark" aria-hidden="true"></span>
    <span>see Capital Renewal</span>
  </div>
  <div class="rule" style="top:654px"></div>
</section>

<section class="card card--back" aria-label="Business card back">
  <svg class="texture" style="left:450px;top:30px" width="234" height="90" role="img" aria-label="Brush-stroke impression of the water feature stones">
    <polygon points="0,80 220,0 234,30 20,90" fill="var(--stroke-tone)" opacity="0.4"/>
  </svg>
  <svg class="texture" style="left:0;top:190px" width="140" height="70" role="img" aria-label="Brush-stroke impression of the water feature stones">
    <polygon points="0,25 130,0 135,30 0,65" fill="var(--stroke-tone)" opacity="0.4"/>
  </svg>
  <svg class="texture" style="left:210px;top:270px" width="474" height="144" role="img" aria-label="Brush-stroke impression of the water feature stones">
    <polygon points="0,144 30,110 474,0 474,144" fill="var(--stroke-tone)" opacity="0.5"/>
  </svg>

  <h2 class="brand brand__line1">Tarrawin's</h2>
  <p class="brand brand__line2">Healing Spring</p>
</section>

</body>
</html>
```